Harbor Compass - Book Cover

I need a book cover for my debut work, "Harbor Compass - Turning the Tide, One Step at a Time." While the website isn't complete, you can get a sense of what I am writing about by looking at my website, harborcompassbooks.org. The book is a leadership development book, but more of a personal change journey. The emphasis is on figuring out how to combine you work, social, and own self into an authentic package that not only resonates with others, but makes what you achieve more fulfilling.

I am attaching a copy of my logo so you can get a sense of what I like. I would prefer to not have the cover be photographic, but am open to suggestions. This will be a series of books so maintaining some sense of style will be important, and can garner future work.

Industry/Entity Type

Leadership

```html
<!DOCTYPE html>
<html lang="en">
<head>
<meta charset="utf-8">
<title>Harbor Compass – Book Cover</title>
<link rel="stylesheet" href="https://fonts.googleapis.com/css2?family=Sorts+Mill+Goudy&family=Source+Sans+3:wght@400&display=swap">
<style>
  :root {
    --paper: #ffffff;
    --ink: #2f2f2f;
    --accent-red: #9b2226;
    --art-gold: #f7c52c;
    --art-orange: #f27a1a;
    --subtitle-ink: #3a3a3a;
  }
  html, body {
    margin: 0;
    padding: 0;
    overflow: hidden;
    background: var(--paper);
  }
  .cover {
    position: relative;
    width: 800px;
    height: 1200px;
    background: var(--paper);
    overflow: hidden;
    font-family: "Sorts Mill Goudy", "Goudy Old Style", serif;
  }
  .cover-art {
    position: absolute;
    left: 322px;
    top: 8px;
    width: 156px;
    height: 330px;
    border-radius: 48% 52% 40% 40% / 38% 38% 62% 62%;
    background: radial-gradient(circle at 50% 40%, var(--art-gold) 0%, #f9a825 45%, var(--art-orange) 100%);
  }
  .title {
    position: absolute;
    left: 0;
    width: 100%;
    margin: 0;
    text-align: center;
    font-weight: 400;
    font-size: 156px;
    line-height: 1;
    letter-spacing: 1px;
  }
  .title-main {
    top: 348px;
    color: var(--ink);
  }
  .title-accent {
    top: 506px;
    color: var(--accent-red);
  }
  .subtitle {
    position: absolute;
    left: 0;
    top: 762px;
    width: 100%;
    margin: 0;
    text-align: center;
    font-size: 44px;
    line-height: 86px;
    letter-spacing: 3px;
    color: var(--subtitle-ink);
  }
  .author {
    position: absolute;
    left: 0;
    top: 1110px;
    width: 100%;
    margin: 0;
    text-align: center;
    font-family: "Source Sans 3", "Myriad Pro", sans-serif;
    font-size: 40px;
    line-height: 1;
    color: var(--accent-red);
  }
</style>
</head>
<body>
  <main class="cover">
    <div class="cover-art" role="img" aria-label="Illustration of a profile silhouette filled with an orange and yellow swirl"></div>
    <h1 class="title title-main">harbor</h1>
    <p class="title title-accent">compass</p>
    <p class="subtitle">Turning the tide,<br>One Step at a Time</p>
    <p class="author">Daniel R. Whitcombe</p>
  </main>
</body>
</html>
```